New College Graduate Resume - Creative and unique design that stands out from the rest

Need creative resume design for recent college graduate who graduated from School of Music with a concentration in music composition and production. Striving for a contemporary layout/design that allows the resume to "be unique" and "stand out" but be polished and professional. Open to integrating moderate color/graphics as part of resume design but the design can be minus those attributes as well. Attached is raw content in 7 sections (name/contact info, education, highlights of qualifications, work experience, honors/awards, and professional affiliations). While the designer has full latitude over overall design which (section headers, font type, separation/spacing, use of bullets, justification of text, etc.) please maintain current order/sequence of the 7 sections.

Industry/Entity Type

School

Requirements
Must have
• Name (Tobias Garrick Elwin III) should be most prominent (bold/font size) compared to remainder of resume copy.
• Section headers should be prominent but less so when compared to name on resume.
• The attached file of resume content is provided as raw source copy and is NOT to be just copied and pasted into open fields as is. Expectation is each section of copy will be organized in a manner that is most visually appealing and may include bullets, appropriate spacing, etc.
Should not have
• The attached file of resume content is provided as source copy and is NOT to be just copied and pasted into open fields as is. Expectation is each section of copy will be organized in a manner that

```html
<!DOCTYPE html>
<html lang="en">
<head>
<meta charset="utf-8">
<title>Tobias Garrick Elwin III – Resume</title>
<link rel="stylesheet" href="https://fonts.googleapis.com/css2?family=Tinos:wght@400;700&family=Marcellus&display=swap">
<style>
  :root {
    --backdrop: #221e1f;
    --page-blue: #0b5ca6;
    --header-light: #2f9be0;
    --header-mid: #1b7cc8;
    --bar-navy: #2a2472;
    --bar-edge: #6aa6dc;
    --bullet: #8cc4f0;
    --text: #ffffff;
  }
  * { margin: 0; padding: 0; box-sizing: border-box; }
  html, body { width: 1200px; height: 849px; overflow: hidden; background: var(--backdrop); }
  body { position: relative; font-family: "Tinos", "Times New Roman", serif; color: var(--text); font-size: 12px; line-height: 13.8px; }

  .page { position: absolute; top: 42px; width: 554px; height: 758px; background: var(--page-blue); overflow: hidden; }
  .page--left { left: 34px; }
  .page--right { left: 613px; }

  .masthead { position: absolute; left: 0; top: 0; width: 554px; height: 60px;
    background: linear-gradient(90deg, var(--header-light) 0%, var(--header-mid) 100%); }
  .masthead__photo { position: absolute; right: 0; top: 0; width: 150px; height: 60px;
    background: radial-gradient(ellipse at 55% 40%, #9fd2f2 0%, #4ea8e0 45%, rgba(30,124,200,0) 80%); }
  .name { position: absolute; left: 30px; top: 12px; font-family: "Marcellus", serif; font-size: 30px; line-height: 36px; white-space: nowrap; }
  .contact { position: absolute; left: 30px; top: 65px; font-size: 12px; white-space: nowrap; }

  .bar { position: absolute; left: 0; width: 554px; height: 19px; background: var(--bar-navy);
    border: 1px solid var(--bar-edge); border-left: none;
    font-weight: 700; font-size: 15px; line-height: 17px; padding-left: 6px; text-transform: uppercase; }
  .bar--light { font-weight: 400; font-size: 16px; }
  .page--right .bar { left: 0; border-left: 1px solid var(--bar-edge); padding-left: 14px; }

  .block { position: absolute; white-space: nowrap; }
  .list { list-style: none; }
  .list li { position: relative; }
  .list li::before { content: ""; position: absolute; left: -13px; top: 3px; width: 8px; height: 8px; background: var(--bullet); }
  .list--spaced li + li { margin-top: 6px; }
  .list--tall li::before { top: 18px; }
  .employer { font-weight: 700; }

  .photo { position: absolute; left: 0; width: 554px; }
  .photo--console-top { top: 0; height: 66px;
    background: linear-gradient(180deg, #5d6f86 0%, #3b4658 40%, #8c98a8 70%, #2d3444 100%); }
  .photo--console-bottom { top: 470px; height: 288px;
    background: linear-gradient(180deg, rgba(11,92,166,1) 0%, rgba(80,130,200,0.85) 30%, #9fb8e0 65%, #d9e4f5 100%); }
</style>
</head>
<body>

<section class="page page--left">
  <header class="masthead">
    <div class="masthead__photo" role="img" aria-label="Close-up photo of a studio microphone"></div>
    <h1 class="name">Tobias Garrick Elwin III</h1>
  </header>
  <p class="contact">218 Wrenfield Court, Atlanta, Georgia&nbsp; 30318 - 404-555-0186 (cell) - tgelwin312@mailbox.com</p>

  <h2 class="bar" style="top:103px">Profile</h2>
  <p class="block" style="left:127px; top:129px">
    Recent graduate of a highly ranked university seeking opportunities to apply<br>
    composition and production talents across a variety of music genres and other<br>
    media. Expertise lies in delivering high quality sound design, editing, mixing, and<br>
    recording. Excellent interpersonal skills and the ability to build strong<br>
    relationships with people at all levels.&nbsp; Exceptionally motivated self-starter and<br>
    creative problem solver who enjoys working collaboratively on teams.
  </p>

  <h2 class="bar" style="top:220px">Education</h2>
  <ul class="block list list--spaced" style="left:127px; top:246px">
    <li>Bayshore University – Caldwell School of Music<br>Coral Springs, Florida</li>
    <li>Bachelor of Music –May 2016<br>Major: Media Writing and Production, GPA 3.20/4.0</li>
    <li>Linden Grove Academy<br>College Park, Georgia<br>High School Diploma with Honors –May 2011</li>
  </ul>

  <h2 class="bar" style="top:364px">Highlights of Qualifications</h2>
  <ul class="block list" style="left:127px; top:391px">
    <li>Media Production Software (TrackForge 11)</li>
    <li>Sound Design</li>
    <li>Sound Acoustics</li>
    <li>Studio Recording</li>
    <li>Audio Editing</li>
    <li>Audio Mixing</li>
    <li>Analog/Digital board operation</li>
    <li>Music Arranging</li>
    <li>Music Composition</li>
    <li>Music Production</li>
    <li>Composing Sheet Music</li>
    <li>Singer-songwriter</li>
    <li>Rhythm guitarist</li>
  </ul>

  <h2 class="bar bar--light" style="top:579px">Work Experience</h2>
  <ul class="block list list--spaced" style="left:127px; top:607px">
    <li><span class="employer">Palmcoast Picture House (PPH)</span><br>Miami, FL<br>May 2014 – Present</li>
    <li><span class="employer">Sound Engineer</span><br>
      Edited and mixed recorded field audio to professional standards.<br>
      Matched audio with motion picture video to create a seamless product.<br>
      Recorded automated dialogue replacement (ADR) audio and integrated into<br>
      motion picture video project using TrackForge 11.Recorded foley sound effects to<br>
      be added to film, video, and othermedia in post-production.<br>
      Composed and recorded original music to accompany various video projects.</li>
  </ul>
</section>

<section class="page page--right">
  <div class="photo photo--console-top" role="img" aria-label="Photo of a studio mixing console seen from above"></div>
  <div class="photo photo--console-bottom" role="img" aria-label="Photo of mixing console faders with a hand adjusting a slider"></div>

  <ul class="block list list--spaced list--tall" style="left:128px; top:90px">
    <li><span class="employer">Northway Retail Corporation</span><br>Atlanta, GA<br>May 2013 - October 2013<br>Sales Associate<br>
      Provided customerservice, maintained a clean and organized work environment,<br>
      assisted in sales, and performed cashier responsibilities.</li>
    <li><span class="employer">Georgia CAN (Civic Action Network)</span><br>Atlanta, GA<br>June 2012 - August 2012<br>On-Site Promoter/Intern<br>
      Promoted and advertised various campaigns and managed various office tasks,<br>
      such as setting up site maps and organizing and sorting non-profit donations.</li>
    <li><span class="employer">Brightline Direct, Incorporated</span><br>Atlanta, GA<br>June 2011 – August 2011<br>Product Marketing Consultant<br>
      Conducted direct sales and marketing of subsidiary product line through<br>
      establishing a compelling value proposition, overcoming objections,and closing<br>
      the sale.</li>
  </ul>

  <h2 class="bar" style="top:376px">Honors/Awards</h2>
  <p class="block" style="left:128px; top:404px">
    Best Film and Score: Frights and Frames 2015 Competition (Bayshore University)<br>
    Harold J Whitcombe Scholar<br>
    Best New Member, Delta Rho Kappa Fraternity, Inc.<br>
    Bayshore University Homecoming King, 2012
  </p>

  <h2 class="bar" style="top:468px">Professional Affiliations</h2>
  <p class="block" style="left:128px; top:496px">
    Member, Guild of Contemporary Composers (GCC)<br>
    Member, National Alliance of Composers, Lyricists, and Publishers (NACLP)<br>
    Member, Sound Engineering Institute (SEI)<br>
    Member, Delta Rho Kappa Fraternity, Incorporated
  </p>
</section>

</body>
</html>
```